Vantrell Law Letterhead

We need a new letterhead design for a Law Firm. The address for the law firm is 4817 Larkspur Boulevard, Suite 250, Houston, Texas 77342. Phone Number: 832-619-3057; Fax Number: 832-407-1694. The logo is uploaded to the project.

```html
<!DOCTYPE html>
<html lang="en">
<head>
<meta charset="utf-8">
<title>Vantrell Law Letterhead</title>
<link href="https://fonts.googleapis.com/css2?family=Montserrat:wght@400;500&display=swap" rel="stylesheet">
<style>
  :root {
    --bg: #e8e8e8;
    --paper: #ffffff;
    --red: #dc1a22;
    --red-deep: #6e0009;
    --navy: #1f3468;
    --ink: #2a2a2a;
    --white: #ffffff;
  }
  * { margin: 0; padding: 0; box-sizing: border-box; }
  html, body {
    width: 1154px; height: 1200px; overflow: hidden;
    background: var(--bg);
    font-family: "Montserrat", Arial, sans-serif;
  }
  .letterhead {
    position: absolute; left: 167px; top: 26px;
    width: 820px; height: 1147px;
    background: var(--paper);
    overflow: hidden;
  }
  .header-band {
    position: absolute; left: 0; top: 0; width: 820px; height: 140px;
    background: linear-gradient(90deg, var(--red) 0%, var(--red) 25%, var(--red-deep) 100%);
  }
  .contact {
    position: absolute; left: 624px; top: 24px;
    color: var(--white); font-size: 13.5px; line-height: 18px;
  }
  .contact .address { margin-bottom: 9px; }
  .contact .line { display: flex; align-items: center; gap: 8px; height: 20px; }
  .contact svg { width: 13px; height: 13px; }
  .brand {
    position: absolute; left: 46px; top: 154px;
    display: flex; align-items: center; gap: 14px;
  }
  .brand-mark { width: 52px; height: 52px; border-radius: 50%; background: var(--navy); }
  .brand-name { font-size: 32px; font-weight: 500; color: var(--navy); letter-spacing: 0.5px; }
  .letter {
    position: absolute; left: 33px; top: 286px; width: 760px;
    color: var(--ink); font-size: 13.4px; line-height: 20.3px;
  }
  .recipient { margin-bottom: 6px; }
  .letter p.body { text-align: justify; margin-bottom: 20.3px; }
  .closing { font-size: 16px; margin-top: 6px; }
  .signature {
    width: 92px; height: 28px; margin-top: 8px;
    background: linear-gradient(90deg, rgba(42,42,42,0.18), rgba(42,42,42,0.06));
    border-radius: 3px;
  }
  .footer-band {
    position: absolute; left: 0; bottom: 0; width: 820px; height: 27px;
    background: linear-gradient(90deg, var(--red) 0%, var(--red) 25%, var(--red-deep) 100%);
  }
</style>
</head>
<body>
<main class="letterhead">
  <div class="header-band" role="img" aria-label="Decorative red and navy wave artwork"></div>

  <div class="contact">
    <div class="address">4817 Larkspur Boulevard,<br>Suite 250, Houston,<br>Texas 77342</div>
    <div class="line">
      <svg viewBox="0 0 24 24" fill="none" stroke="#fff" stroke-width="2.2"><path d="M5 3h4l2 5-2.5 1.5a11 11 0 0 0 6 6L16 13l5 2v4a2 2 0 0 1-2 2A16 16 0 0 1 3 5a2 2 0 0 1 2-2z"/></svg>
      <span>832-619-3057</span>
    </div>
    <div class="line">
      <svg viewBox="0 0 24 24" fill="#fff"><rect x="6" y="2" width="12" height="6" rx="1"/><rect x="2" y="9" width="20" height="9" rx="2"/><rect x="6" y="15" width="12" height="7" rx="1" fill="#fff" stroke="#a00" stroke-width="1.5"/></svg>
      <span>832-407-1694</span>
    </div>
  </div>

  <div class="brand">
    <div class="brand-mark"></div>
    <div class="brand-name">Vantrell Law</div>
  </div>

  <section class="letter">
    <div class="recipient">Mr/s<br>First Name and Last Name<br>Company Name<br>Address</div>
    <p class="body">Lorem ipsum dolor sit amet,consectetur adipiscing sed do eiusmod tempor incididunt laboreet dolore magna aliqua.Ut enim ad minim.veniam, quis nostrud exercitation ullamco laboris nisi ut aliquip exea commodo consequat.Lorem ipsum dolor sit amet,consectetur adipiscing sed do eiusmod tempor incididunt.labore et dolore magna aliqua. Ut enim</p>
    <p class="body">Lorem ipsum dolor sit amet, consectetur adipiscing sed do eiusmod tempor incididunt labore et dolore magna aliqua. Ut enim ad minim veniam, quis nostrud exercitation ullamco laboris nisi ut aliquip exea commodo consequat.Duis aute irure dolor in reprehenderit in voluptate velit esse cillum irure dolor in reprehenderit in voluptate velit esse irure</p>
    <p class="body">Lorem ipsum dolor sit amet, consectetur adipiscing sed do eiusmod tempor incididunt labore et dolore magna aliqua. consequat. Duis aute irure dolor in.reprehenderit in voluptate velit esse cillum dolore eu fugiat nulla pariatur. Excepteur sint occaecat cupidatat non proident, sunt in culpa qui officia deserunt mollit,</p>
    <p class="body">Lorem ipsum dolor sit amet, consectetur adipiscing sed do eiusmod tempor incididunt labore et dolore magna aliqua. Ut enim Lorem ipsum dolor sit amet, consectetur adipiscing sed do eiusmod tempor incididunt labore et dolore magna aliqua. Ut enim Lorem ipsum aliqua.ipsum</p>
    <p class="body">Lorem ipsum dolor sit amet, consectetur adipiscing sed do eiusmod tempor incididunt labore et dolore magna aliqua. Ut enim ad minim veniam, quis nostrud exercitation ullamco laboris nisi ut aliquip exea commodo consequat.Duis aute irure dolor in reprehenderit in voluptate velit esse cillum irure dolor in reprehenderit in voluptate velit esse irure</p>
    <p class="body">Lorem ipsum dolor sit amet, consectetur adipiscing sed do eiusmod tempor incididunt labore et dolore magna aliqua. Ut enim ad minim veniam, quis nostrud exercitation ullamco laboris nisi ut aliquip exea commodo consequat.Duis aute irure dolor in reprehenderit in voluptate velit esse cillum irure dolor in reprehenderit in voluptate velit esse irure</p>
    <div class="closing">Regards</div>
    <div class="signature" role="img" aria-label="Handwritten signature"></div>
  </section>

  <div class="footer-band"></div>
</main>
</body>
</html>
```